Letterhead and email signiture

Hello,

I have an example of a letterhead that we need. The one we have constandly moves if we paste any information in it. We are looking for one that is permanent. We only need the top of the letterhead on the first page but the bottom on each and every page afterward.

It does not have to be exactly what I am providing here. Please take a look at the website and maybe you will have a better idea.

We are looking to do something similar for an email signature

Maplerockllc.com

```html
<!DOCTYPE html>
<html lang="en">
<head>
<meta charset="utf-8">
<title>Maple Rock LLC — Letterhead and Email Signature</title>
<link href="https://fonts.googleapis.com/css2?family=Roboto:wght@400;700&display=swap" rel="stylesheet">
<style>
  :root {
    --backdrop: #3b3b3d;
    --paper: #f5f3f4;
    --ink: #1a1a1a;
    --body-ink: #5a5a5a;
    --accent-blue: #3a86d4;
    --bar-black: #000000;
    --bar-grey: #8d8d8d;
    --mark-fill: #4a7fc1;
  }
  * { box-sizing: border-box; margin: 0; padding: 0; }
  html, body { width: 1200px; height: 826px; overflow: hidden; }
  body {
    background: var(--backdrop);
    font-family: "Roboto", Arial, sans-serif;
    position: relative;
  }
  .sheet {
    position: absolute;
    background: var(--paper);
    box-shadow: 0 2px 8px rgba(0,0,0,0.35);
  }
  .letterhead { left: 67px; top: 72px; width: 495px; height: 698px; }
  .signature-card { left: 626px; top: 327px; width: 504px; height: 137px; }

  .company-name {
    position: absolute;
    font-weight: 700;
    color: var(--ink);
    letter-spacing: -0.3px;
    white-space: nowrap;
  }
  .letterhead .company-name { left: 47px; top: 58px; font-size: 19px; }
  .signature-card .company-name { left: 38px; top: 48px; font-size: 23px; }

  .contact-list { position: absolute; list-style: none; color: var(--ink); }
  .contact-list li { display: flex; align-items: center; white-space: nowrap; }
  .contact-list svg { flex: none; fill: var(--accent-blue); }
  .letterhead .contact-list { left: 345px; top: 53px; font-size: 8px; line-height: 10px; }
  .letterhead .contact-list svg { width: 7px; height: 7px; margin-right: 5px; }
  .signature-card .contact-list { left: 284px; top: 50px; font-size: 10px; line-height: 12.5px; }
  .signature-card .contact-list svg { width: 8px; height: 8px; margin-right: 8px; }

  .letter-greeting {
    position: absolute; left: 50px; top: 170px;
    font-size: 14px; color: #333;
  }
  .letter-body {
    position: absolute; left: 50px; top: 211px; width: 399px;
    font-size: 8.1px; line-height: 11.8px; color: var(--body-ink);
    text-align: justify;
  }
  .letter-body p + p { margin-top: 12px; }
  .letter-closing {
    position: absolute; left: 50px; top: 472px;
    font-size: 8px; color: var(--body-ink);
  }
  .signature-mark {
    position: absolute; left: 47px; top: 492px; width: 64px; height: 25px;
    background: linear-gradient(180deg, rgba(30,40,70,0) 30%, rgba(30,40,70,0.35) 50%, rgba(30,40,70,0) 70%);
  }
  .signer-name {
    position: absolute; left: 52px; top: 529px;
    font-size: 11px; color: #333;
  }
  .signer-role {
    position: absolute; left: 52px; top: 545px;
    font-size: 8px; color: #444;
  }

  .footer-bar {
    position: absolute; height: 16px;
    display: flex; align-items: center;
  }
  .footer-bar .bar-black {
    height: 100%; background: var(--bar-black); color: #fff;
    display: flex; align-items: center; white-space: nowrap;
  }
  .footer-bar .bar-grey { height: 100%; flex: 1; background: var(--bar-grey); }
  .footer-bar .bar-dot {
    position: absolute; width: 20px; height: 20px; border-radius: 50%;
    background: var(--mark-fill); border: 2px solid #fff; top: -2px;
  }
  .letterhead .footer-bar { left: -3px; top: 666px; width: 500px; }
  .letterhead .bar-black { width: 562px; padding-left: 37px; font-size: 7.8px; width: 438px; }
  .letterhead .bar-dot { left: 428px; }
  .signature-card .footer-bar { left: 0; top: 113px; width: 504px; }
  .signature-card .bar-black { width: 438px; padding-left: 38px; font-size: 10px; }
  .signature-card .bar-dot { left: 437px; }

  .divider {
    position: absolute; left: 263px; top: 45px; width: 1px; height: 33px;
    background: var(--ink);
  }
</style>
</head>
<body>

<svg width="0" height="0" style="position:absolute" aria-hidden="true">
  <defs>
    <symbol id="icon-phone" viewBox="0 0 10 10">
      <path d="M2.2 0.6 L3.6 2.4 L2.8 3.4 C3.4 4.8 5.2 6.6 6.6 7.2 L7.6 6.4 L9.4 7.8 L8.4 9.4 C4.6 9.2 0.8 5.4 0.6 1.6 Z"/>
    </symbol>
    <symbol id="icon-mail" viewBox="0 0 10 10">
      <path d="M0.5 2 H9.5 V8 H0.5 Z M1.2 2.6 L5 5.4 L8.8 2.6" stroke="#fff" stroke-width="0.6"/>
    </symbol>
    <symbol id="icon-web" viewBox="0 0 10 10">
      <circle cx="5" cy="5" r="4.5"/>
      <path d="M0.5 5 H9.5 M5 0.5 C3 3 3 7 5 9.5 M5 0.5 C7 3 7 7 5 9.5" stroke="#fff" stroke-width="0.6" fill="none"/>
    </symbol>
  </defs>
</svg>

<section class="sheet letterhead" aria-label="Letterhead">
  <div class="company-name">MAPLE ROCK LLC</div>
  <ul class="contact-list">
    <li><svg><use href="#icon-phone"/></svg>555-214-0187</li>
    <li><svg><use href="#icon-mail"/></svg>555-386-0242</li>
    <li><svg><use href="#icon-web"/></svg>www.maplerockllc.com</li>
  </ul>

  <p class="letter-greeting">Dear Mr. Hollis,</p>
  <div class="letter-body">
    <p>Lorem ipsum dolor sit amet, consectetur adipiscing elit. Donec orci purus, luctus vitae dignissim eu, iaculis sed purus. Vivamus faucibus, ipsum nec aliquet viverra, leo mauris condimentum ligula, sit amet sagittis enim ligula quis arcu. Nam egestas tortor id nisi porttitor mattis. In tortor ante, ultricies in suscipit a, tempus non massa. Vivamus et auctor mi. Fusce vel massa nulla. Phasellus nec eros mauris, et scelerisque orci.</p>
    <p>Donec malesuada orci vitae nulla accumsan porta a id massa. Quisque accumsan iaculis magna sit amet fringilla. Maecenas consequat, magna eget tincidunt semper, odio nibh rutrum mi, id feugiat ante nisi eu risus. Vestibulum nunc orci, rhoncus a placerat in, ultricies in mi. Cras mattis varius eros, vel fringilla nisi suscipit eget. Quisque scelerisque sagittis nulla at porttitor.</p>
    <p>Sed id augue vitae urna euismod commodo aliquet a quam. Pellentesque arcu velit, cursus et malesuada ut, consequat et diam. Nullam erat sem, rhoncus id ullamcorper vitae, rhoncus et arcu. In ultricies ultricies nulla, ut rutrum nisi iaculis at. Donec eu magna a metus ornare faucibus. Fusce aliquet faucibus ultricies. Morbi semper, est id tincidunt gravida, sem arcu adipiscing lacus, ac bibendum nulla leo eu purus. Quisque nec diam sed risus consectetur a ccumsan quis quis nibh. Vestibulum id purus lorem.</p>
    <p>It is a long established fact that a reader will be distracted by the readable content of a page when looking at its layout. The point of using Lorem Ipsum is that it has a more-or-less normal distribution of letters, as opposed to using 'Content here, content here', making it look like readable English. Many desktop publishing packages</p>
  </div>
  <p class="letter-closing">Sincerely,</p>
  <div class="signature-mark" role="img" aria-label="Handwritten signature"></div>
  <p class="signer-name">Evan Hollis</p>
  <p class="signer-role">CEO/ Founder</p>

  <div class="footer-bar">
    <div class="bar-black">This document is confidential and intended solely for investigative purposes by Maple Rock LLC.</div>
    <div class="bar-grey"></div>
    <span class="bar-dot"></span>
  </div>
</section>

<section class="sheet signature-card" aria-label="Email signature">
  <div class="company-name">MAPLE ROCK LLC</div>
  <div class="divider"></div>
  <ul class="contact-list">
    <li><svg><use href="#icon-phone"/></svg>555-214-0187</li>
    <li><svg><use href="#icon-mail"/></svg>555-386-0242</li>
  </ul>
  <div class="footer-bar">
    <div class="bar-black">www.maplerockllc.com</div>
    <div class="bar-grey"></div>
    <span class="bar-dot"></span>
  </div>
</section>

</body>
</html>
```